Visitenkarten
Zielgruppe
Hallo!
Für mein Unternehmen habe ich bereits einmal ein Logo mit Tintenkrug erstellen lassen (leider weiß ich den Designer nicht mehr).
Unter meinem Unternehmen Vollmerhaus Coaching laufen zwei Unternehmensbereiche, für die ich jetzt Visitenkarten benötige. Daher ist der Stil der beiden Teilbereiche ähnlich. Die Logos existieren schon. Nun benötige ich für beide Bereiche Visitenkarten. Für beide Bereiche benötige ich im Anschluss im 1:1 Auftrage noch Dateien, damit die ich Logos auch gut auf Webseiten und Social Medien nutzen kann.
Vollmerhaus HR Services <: bietet HR Dienstleistungen rund um das Personalwesen an: HR-Trainings, HR Outsourcing und Projekt- und Interimsmanagement
Klarer Sattel | Vollmerhaus Coaching: bietet Mental- und Hypnosecoachings an, Trainings zur mentalen Fitness, Stress- und Blockadenlösung im Reitsport und optimale Turniervorbereitung
Aufgabenstellung
Bitte den bestehenden Brandguide und die Materialien nutzen. Eigene Ideen sind willkommen, sollen aber in der Logik bleiben.
Daten Visitenkarte Vollmerhaus HR Services:
Henrike Vollmerhaus
Dipl. Sozialwirt, Business Coach, Mentaltrainer
Telefon +49 (0)1577 32 58 406
Mobil +49 (0)160 92 37 584
Mail: henrike@vollmerhaus-beratung.example
Vollmerhaus HR Services | Vollmerhaus Coaching
Am Lindenhang 9b
29715 Heidebrück
Daten Visitenkarte Vollmerhaus Klarer Sattel:
Dipl. Sozialwirt, Hypnosecoach, Mentaltrainer
Klarer Sattel | Vollmerhaus Coaching

```html
<!DOCTYPE html>
<html lang="de">
<head>
<meta charset="utf-8">
<title>Visitenkarte Klarer Sattel</title>
<link rel="stylesheet" href="https://fonts.googleapis.com/css2?family=Jost:wght@400;500&family=Josefin+Sans:wght@300&display=swap">
<style>
  :root {
    --violet: #635ca4;
    --lavender: #b3acd6;
    --lavender-soft: #a69fd0;
    --paper: #ffffff;
    --backdrop: #e4e4e6;
  }
  * { margin: 0; padding: 0; box-sizing: border-box; }
  html, body { width: 1200px; height: 1200px; overflow: hidden; }
  body { background: var(--backdrop); position: relative; font-family: "Josefin Sans", sans-serif; }

  .card { position: absolute; left: 250px; width: 700px; height: 463px; overflow: hidden; }
  .card--front { top: 109px; background: var(--violet); }
  .card--back { top: 623px; background: var(--paper); }

  .horse-art { position: absolute; border-radius: 40% 45% 30% 30%; }
  .card--front .horse-art {
    left: 117px; top: 105px; width: 195px; height: 273px;
    background: linear-gradient(160deg, #ffffff 0%, #d5d1ec 55%, #b3acd6 100%);
    opacity: .55;
  }
  .card--back .horse-art {
    left: 470px; top: 20px; width: 206px; height: 278px;
    background: linear-gradient(160deg, #8a84c0 0%, #c4bfe2 55%, #e6e3f4 100%);
    opacity: .6;
  }

  .brand-name {
    position: absolute; left: 318px; top: 188px; width: 252px;
    text-align: center; color: var(--paper);
    font-family: "Jost", sans-serif; font-weight: 500;
    text-transform: uppercase;
  }
  .brand-name .line { display: block; }
  .brand-name .line--main { font-size: 31px; line-height: 1.2; letter-spacing: .3px; }
  .brand-name .line--small { margin-top: 10px; font-size: 17px; line-height: 1.3; letter-spacing: 1px; }

  .person { position: absolute; left: 94px; top: 160px; font-family: "Jost", sans-serif; }
  .person__name { font-size: 25px; font-weight: 400; color: var(--violet); letter-spacing: -.3px; text-transform: uppercase; line-height: 1; }
  .person__first { color: var(--lavender-soft); }
  .person__title { margin-top: 4px; font-size: 10px; color: var(--lavender-soft); letter-spacing: .4px; text-transform: uppercase; }

  .contact { position: absolute; left: 0; top: 0; width: 100%; height: 100%; list-style: none; }
  .contact__item { position: absolute; left: 135px; color: var(--violet); font-weight: 300; font-size: 20px; line-height: 1.1; white-space: nowrap; }
  .contact__item--phone { top: 231px; letter-spacing: 1.6px; }
  .contact__item--mobile { top: 267px; letter-spacing: 1.6px; }
  .contact__item--mail { top: 307px; }
  .contact__item--address { top: 346px; line-height: 1.15; }
  .contact__icon { position: absolute; left: -50px; top: -2px; width: 24px; height: 24px; fill: var(--lavender); }
  .contact__item--address .contact__icon { top: 12px; }
</style>
</head>
<body>
  <section class="card card--front">
    <div class="horse-art" role="img" aria-label="Skizzierte Illustration eines galoppierenden Pferdes in Weiß und Lavendel"></div>
    <div class="brand-name">
      <span class="line line--main">Klarer Sattel</span>
      <span class="line line--small">by Vollmerhaus Coaching</span>
    </div>
  </section>

  <section class="card card--back">
    <div class="horse-art" role="img" aria-label="Skizzierte Illustration eines galoppierenden Pferdes in Violett und Lavendel"></div>
    <div class="person">
      <p class="person__name"><span class="person__first">Henrike</span> Vollmerhaus</p>
      <p class="person__title">Dipl. Sozialwirt, Business Coach, Mentaltrainer</p>
    </div>
    <ul class="contact">
      <li class="contact__item contact__item--phone">
        <svg class="contact__icon" viewBox="0 0 24 24"><path d="M6.6 10.8a15.2 15.2 0 0 0 6.6 6.6l2.2-2.2a1 1 0 0 1 1-.25 11.4 11.4 0 0 0 3.6.57 1 1 0 0 1 1 1V20a1 1 0 0 1-1 1A17 17 0 0 1 3 4a1 1 0 0 1 1-1h3.5a1 1 0 0 1 1 1c0 1.25.2 2.45.57 3.570a1 1 0 0 1-.25 1z"/></svg>
        +49 (0)1577 32 58 406
      </li>
      <li class="contact__item contact__item--mobile">
        <svg class="contact__icon" viewBox="0 0 24 24"><path d="M5 1h9a2 2 0 0 1 2 2v18a2 2 0 0 1-2 2H5a2 2 0 0 1-2-2V3a2 2 0 0 1 2-2zm0 3v14h9V4zm4.5 15.5a1 1 0 1 0 0 2 1 1 0 0 0 0-2z"/><path d="M18 9c1 1 1 5 0 6l-.8-.6c.7-.8.7-4 0-4.8zm2.2-1.5c1.8 2 1.8 7 0 9l-.8-.6c1.4-1.6 1.4-6.2 0-7.8z"/></svg>
        +49 (0)160 92 37 584
      </li>
      <li class="contact__item contact__item--mail">
        <svg class="contact__icon" viewBox="0 0 24 24"><path d="M1 5h22v14H1zm2 1.8v.2l9 6 9-6v-.2zm0 2.4V17h18V9.2l-9 6z"/></svg>
        henrike@vollmerhaus-beratung.example
      </li>
      <li class="contact__item contact__item--address">
        <svg class="contact__icon" viewBox="0 0 24 24"><path d="M12 1a8 8 0 0 0-8 8c0 6 8 14 8 14s8-8 8-14a8 8 0 0 0-8-8zm0 11a3 3 0 1 1 0-6 3 3 0 0 1 0 6z"/></svg>
        Vollmerhaus HR Services | Vollmerhaus Coaching<br>
        Am Lindenhang 9b<br>
        29715 Heidebrück
      </li>
    </ul>
  </section>
</body>
</html>
```